Brisk Harbor Funding - Letterhead

We need letterhead options for our case funding company called Brisk Harbor Funding. Here are some of the details:

Name - Brisk Harbor Funding
Phone - (555) 214 - 9083
Address - 38 Larkmoor Avenue
Suite 412
New York, NY 10958
Website - briskharborfunding.example

```html
<!DOCTYPE html>
<html lang="en">
<head>
<meta charset="utf-8">
<title>Brisk Harbor Funding – Letterhead</title>
<link rel="stylesheet" href="https://fonts.googleapis.com/css2?family=Montserrat:wght@600&family=Mulish:wght@400&display=swap">
<style>
  :root {
    --backdrop: #d9d9d9;
    --paper: #f4f4f4;
    --paper-shade: #e3e3e3;
    --navy: #14283f;
    --slate: #4f5e69;
    --ink: #2b3440;
    --white: #ffffff;
  }
  html, body {
    margin: 0;
    padding: 0;
    width: 1200px;
    height: 780px;
    overflow: hidden;
    background: var(--backdrop);
  }
  .letterhead {
    position: absolute;
    left: 335px;
    top: 15px;
    width: 530px;
    height: 750px;
    background: linear-gradient(160deg, var(--paper) 0%, var(--paper-shade) 100%);
    overflow: hidden;
  }
  .brand {
    position: absolute;
    left: 38px;
    top: 48px;
    display: flex;
    align-items: center;
    gap: 8px;
  }
  .brand-dot {
    width: 14px;
    height: 14px;
    border-radius: 50%;
    background: var(--navy);
  }
  .brand-name {
    font-family: "Montserrat", sans-serif;
    font-weight: 600;
    font-size: 10.5px;
    line-height: 11.5px;
    letter-spacing: 0.9px;
    color: var(--navy);
    text-transform: uppercase;
  }
  .contact {
    position: absolute;
    left: 366px;
    top: 93px;
    display: flex;
    align-items: stretch;
    gap: 5px;
  }
  .contact-icons {
    display: flex;
    flex-direction: column;
    gap: 3px;
    padding-top: 1px;
  }
  .contact-rule {
    width: 1.5px;
    background: var(--navy);
  }
  .contact-lines {
    font-family: "Mulish", sans-serif;
    font-size: 8px;
    line-height: 11px;
    color: var(--ink);
  }
  .base-band {
    position: absolute;
    left: 0;
    bottom: 0;
    width: 380px;
    height: 6px;
    background: var(--slate);
  }
  .web-tab {
    position: absolute;
    right: 0;
    bottom: 0;
    width: 156px;
    height: 24px;
  }
  .web-address {
    position: absolute;
    right: 16px;
    bottom: 6px;
    font-family: "Mulish", sans-serif;
    font-size: 8px;
    color: var(--white);
  }
</style>
</head>
<body>
  <main class="letterhead">
    <header class="brand">
      <span class="brand-dot"></span>
      <div class="brand-name">Brisk<br>Harbor<br>Funding</div>
    </header>

    <address class="contact" style="font-style:normal">
      <div class="contact-icons">
        <svg width="8" height="8" viewBox="0 0 24 24" aria-hidden="true">
          <path fill="#14283f" d="M6.6 10.8a15 15 0 0 0 6.6 6.6l2.2-2.2a1 1 0 0 1 1-.25 11.4 11.4 0 0 0 3.6.57 1 1 0 0 1 1 1V20a1 1 0 0 1-1 1A17 17 0 0 1 3 4a1 1 0 0 1 1-1h3.5a1 1 0 0 1 1 1c0 1.25.2 2.45.57 3.6a1 1 0 0 1-.25 1z"/>
        </svg>
        <svg width="8" height="9" viewBox="0 0 24 24" aria-hidden="true">
          <path fill="#14283f" d="M12 2a7 7 0 0 0-7 7c0 5.2 7 13 7 13s7-7.8 7-13a7 7 0 0 0-7-7zm0 9.5A2.5 2.5 0 1 1 12 6.5a2.5 2.5 0 0 1 0 5z"/>
        </svg>
      </div>
      <span class="contact-rule"></span>
      <div class="contact-lines">
        (555) 214 - 9083<br>
        38 Larkmoor Avenue<br>
        Suite 412, New York, NY 10958
      </div>
    </address>

    <footer>
      <span class="base-band"></span>
      <svg class="web-tab" viewBox="0 0 156 24" preserveAspectRatio="none" aria-hidden="true">
        <path fill="#14283f" d="M0 24 L8 6 Q11 0 18 0 L156 0 L156 24 Z"/>
      </svg>
      <span class="web-address">www.briskharborfunding.example</span>
    </footer>
  </main>
</body>
</html>
```